Copperfen Hollow Wine And Spirits

We need to design a website for our Liquor Store

Industry/Entity Type

Store

Number of Pages Required

4 page

Requirements
Must have
• Beer, Liquor, Wine & Cigar related theme.
• Mention our 8-locations addresses & maps info
Nice to have
• category for Beer, Liquor & Wine to setup database for item list to link our sql server database.

```html
<!DOCTYPE html>
<html lang="en">
<head>
<meta charset="utf-8">
<title>Copperfen Hollow Wine And Spirits</title>
<link href="https://fonts.googleapis.com/css2?family=Open+Sans:ital,wght@0,400;0,600;0,700;1,400&display=swap" rel="stylesheet">
<style>
:root{
  --blue:#1f4ea3;
  --blue-dark:#173d84;
  --yellow:#f5d630;
  --ink:#1b1b1b;
  --muted:#666;
  --grey-bg:#efefef;
  --line:#d9d9d9;
  --footer:#0c0c0c;
  --white:#fff;
  --icon:#6e6e6e;
}
*{box-sizing:border-box;margin:0;padding:0}
html,body{width:1200px;height:5187px;overflow:hidden}
body{font-family:"Open Sans",Arial,sans-serif;color:var(--ink);background:var(--white);font-size:14px;line-height:1.5}
.container{width:990px;margin:0 auto;position:relative}
.section-title{text-align:center;font-size:30px;font-weight:700}
.section-sub{text-align:center;font-size:13px;color:var(--muted);margin-top:4px}
.section-title.light,.section-sub.light{color:var(--white)}
.title-rule{width:60px;height:3px;background:var(--yellow);margin:10px auto 0}

/* top bar */
.top-bar{height:34px;background:var(--blue-dark);color:var(--white);font-size:13px;font-weight:600}
.top-bar .container{display:flex;justify-content:space-between;align-items:center;height:34px}
.top-links{display:flex;gap:30px}

/* header */
.site-header{height:166px;background:#f2f2f2}
.site-header .container{display:flex;align-items:center;justify-content:space-between;height:166px}
.phone{display:flex;align-items:center;gap:18px;font-size:30px;font-style:italic;color:var(--ink)}
.brand{display:flex;align-items:center;gap:12px;font-size:28px;font-weight:700;color:var(--blue)}
.brand-square{width:22px;height:22px;background:var(--yellow)}
.cart{display:flex;align-items:center;gap:14px;font-size:13px;line-height:1.3}

/* nav */
.main-nav{height:52px;background:var(--yellow)}
.main-nav .container{display:flex;align-items:center;justify-content:space-between;height:52px}
.nav-list{display:flex;gap:38px;list-style:none;font-size:14px;font-weight:700;color:var(--ink)}
.search{width:225px;height:36px;background:var(--blue);color:var(--white);font-size:13px;font-weight:600;display:flex;align-items:center;padding-left:12px}

/* hero */
.hero{height:457px;background:linear-gradient(100deg,#1a120e 0%,#3a2a20 45%,#24170f 75%,#120c09 100%);position:relative}
.hero-photo{position:absolute;inset:0}
.hero .container{padding-top:120px}
.hero-title{font-size:40px;color:var(--white);font-weight:400}
.btn{display:inline-block;background:var(--blue);color:var(--white);font-size:14px;font-weight:600;padding:12px 26px;margin-top:60px}

/* intro */
.intro{height:536px;padding-top:62px}
.intro-body{display:flex;justify-content:space-between;align-items:center;margin-top:90px}
.intro-text{width:520px;font-size:13px;color:#333}
.intro-text p+p{margin-top:24px}
.intro-brand{width:350px;height:300px;display:flex;align-items:center;justify-content:center;gap:12px;font-size:30px;font-weight:700;color:var(--blue)}

/* locations */
.locations{height:823px;background:linear-gradient(180deg,#1d140f 0%,#3b2a1f 50%,#231812 100%);padding-top:70px}
.location-grid{display:grid;grid-template-columns:repeat(4,225px);justify-content:space-between;row-gap:35px;margin-top:80px}
.location-card{height:260px;background:var(--white);padding:22px 20px}
.location-card h3{font-size:20px;font-weight:600;margin-bottom:14px}
.loc-row{display:flex;gap:8px;font-size:13px;color:#333;margin-bottom:10px}
.loc-row svg{flex:none;margin-top:3px}
.map-link{font-size:13px;font-weight:600;color:var(--blue);margin-top:14px;display:block}

/* liquor categories */
.categories{height:473px;padding-top:70px}
.category-list{display:flex;justify-content:space-between;width:880px;margin:80px auto 0}
.category{width:160px;text-align:center;font-size:15px;color:#333}
.category svg{display:block;margin:0 auto 30px}

/* testimonials */
.testimonials{height:295px;background:linear-gradient(90deg,#2d2d2d 0%,#5b5550 50%,#2a2a2a 100%);position:relative;padding-top:30px}
.quote-badge{width:44px;height:44px;border-radius:50%;border:2px solid var(--yellow);margin:0 auto;display:flex;align-items:center;justify-content:center;color:var(--yellow);font-weight:700;font-size:20px}
.testimonial-list{display:flex;justify-content:space-between;margin-top:40px}
.testimonial{width:300px}
.testimonial-head{display:flex;gap:14px;align-items:center}
.avatar{width:74px;height:74px;border-radius:50%;background:linear-gradient(135deg,#b08a6a,#4a3526);flex:none}
.testimonial p{font-size:12px;color:var(--white);line-height:1.45}
.testimonial .name{font-size:12px;color:var(--white);margin-top:12px;padding-left:10px}
.dots{display:flex;justify-content:center;gap:12px;margin-top:30px}
.dots span{width:48px;height:5px;background:var(--white)}
.dots span:first-child{background:var(--yellow)}

/* products */
.products{height:1175px;padding-top:70px}
.product-grid{display:grid;grid-template-columns:repeat(3,310px);justify-content:space-between;row-gap:35px;margin-top:80px}
.product-card{height:415px;border:1px solid var(--line);text-align:center;padding-top:60px}
.product-photo{width:200px;height:170px;margin:0 auto;background:radial-gradient(ellipse at 50% 60%,#3a3a3a 0%,#bdbdbd 55%,#fff 75%)}
.product-name{font-size:17px;margin-top:34px;line-height:1.35}
.price{font-size:20px;font-weight:700;color:var(--blue);margin-top:18px}

/* blog */
.blog{height:795px;background:var(--grey-bg);padding-top:60px}
.blog .section-sub{width:900px;margin:8px auto 0;font-size:13px}
.blog-grid{display:flex;justify-content:space-between;width:1030px;margin:50px auto 0}
.post{width:330px}
.post-photo{height:230px}
.post-meta{font-size:13px;margin-top:20px;line-height:1.4}
.post-meta .date{color:var(--muted)}
.post p{font-size:12px;color:#333;margin-top:14px}
.read-more{font-size:13px;font-weight:600;color:var(--blue);margin-top:12px;display:block}

/* footer */
.site-footer{height:312px;background:var(--footer);color:var(--white);padding-top:40px}
.footer-cols{display:flex;justify-content:space-between}
.footer-col{width:220px}
.footer-col h4{font-size:18px;font-weight:700;margin-bottom:18px}
.footer-col p{font-size:12px;line-height:1.55}
.footer-col ul{list-style:none;font-size:12px}
.footer-col li{display:flex;align-items:center;gap:10px;margin-bottom:6px}
.footer-col li::before{content:"";width:6px;height:6px;background:var(--white);border-radius:50%}
.contact-line{display:flex;gap:10px;font-size:12px;margin-bottom:16px}
.bottom-bar{height:69px;background:var(--blue-dark);color:var(--white);font-size:13px}
.bottom-bar .container{display:flex;justify-content:space-between;align-items:center;height:69px}
.socials{display:flex;gap:10px}
.socials span{width:26px;height:26px;border-radius:50%;background:#3a66b8}
</style>
</head>
<body>

<div class="top-bar">
  <div class="container">
    <span>One Stop Wine &amp; Spirits Solutions</span>
    <div class="top-links"><span>My Account</span><span>Login</span><span>Register</span></div>
  </div>
</div>

<header class="site-header">
  <div class="container">
    <div class="phone">
      <svg width="34" height="34" viewBox="0 0 24 24"><path fill="#1f4ea3" d="M6.6 10.8a15.1 15.1 0 0 0 6.6 6.6l2.2-2.2c.3-.3.7-.4 1-.2 1.1.4 2.3.6 3.6.6.6 0 1 .4 1 1V20c0 .6-.4 1-1 1A17 17 0 0 1 3 4c0-.6.4-1 1-1h3.5c.6 0 1 .4 1 1 0 1.3.2 2.5.6 3.6.1.3 0 .7-.2 1z"/></svg>
      <span>123-456-783</span>
    </div>
    <div class="brand"><span class="brand-square"></span>Copperfen Hollow</div>
    <div class="cart">
      <svg width="40" height="34" viewBox="0 0 24 20"><path fill="#1f4ea3" d="M0 1h4l3 11h12l3-8H6.5L6 3H24v2l-4 9H6L2.5 3H0z"/><circle cx="8" cy="17" r="2" fill="#1f4ea3"/><circle cx="18" cy="17" r="2" fill="#1f4ea3"/></svg>
      <div>Your Cart<br>0 items $0.00</div>
    </div>
  </div>
</header>

<nav class="main-nav">
  <div class="container">
    <ul class="nav-list"><li>HOME</li><li>FINE WINES</li><li>SPIRITS</li><li>COLD BEERS</li><li>CIGARS</li><li>ABOUT US</li><li>CONTACT US</li></ul>
    <div class="search">Search your liquor</div>
  </div>
</nav>

<section class="hero">
  <div class="hero-photo" role="img" aria-label="Wine bottle and filled glass with grapes on a dark wooden table"></div>
  <div class="container">
    <h1 class="hero-title">one stop wine and spirits solutions</h1>
    <span class="btn">Know more</span>
  </div>
</section>

<section class="intro">
  <div class="container">
    <h2 class="section-title">Lorem Ipsum</h2>
    <p class="section-sub">Lorem ipsum dolor sit amet</p>
    <div class="intro-body">
      <div class="intro-text">
        <p>Lorem ipsum dolor sit amet, consectetur adipiscing elit, sed do eiusmod tempor incididunt ut labore et dolore magna aliqua. Ut enim ad minim veniam, quis nostrud exercitation ullamco laboris nisi ut aliquip ex ea commodo consequat duis aute irure dolor.</p>
        <p>Duis aute irure dolor in reprehenderit in voluptate velit esse cillum dolore eu fugiat nulla pariatur. Excepteur sint occaecat cupidatat non proident, sunt in culpa qui officia deserunt.</p>
      </div>
      <div class="intro-brand"><span class="brand-square"></span>Copperfen Hollow</div>
    </div>
  </div>
</section>

<section class="locations">
  <div class="container">
    <h2 class="section-title light">Our Location</h2>
    <p class="section-sub light">Lorem ipsum dolor sit amet</p>
    <div class="location-grid">
      <!-- 8 store cards -->
      <div class="location-card"><h3>Location 1</h3>
        <div class="loc-row"><svg width="12" height="14" viewBox="0 0 12 16"><path fill="#555" d="M6 0a6 6 0 0 0-6 6c0 4.5 6 10 6 10s6-5.5 6-10a6 6 0 0 0-6-6zm0 8.5A2.5 2.5 0 1 1 6 3.5a2.5 2.5 0 0 1 0 5z"/></svg><span>12 Hollow Street, Suite 4, Riverside Park, NY 10001</span></div>
        <div class="loc-row"><svg width="12" height="12" viewBox="0 0 24 24"><path fill="#555" d="M6.6 10.8a15 15 0 0 0 6.6 6.6l2.2-2.2c.3-.3.7-.4 1-.2 1.1.4 2.3.6 3.6.6.6 0 1 .4 1 1V20c0 .6-.4 1-1 1A17 17 0 0 1 3 4c0-.6.4-1 1-1h3.5c.6 0 1 .4 1 1 0 1.3.2 2.5.6 3.6.1.3 0 .7-.2 1z"/></svg><span>123-456-783</span></div>
        <span class="map-link">View Map</span></div>
      <div class="location-card"><h3>Location 2</h3>
        <div class="loc-row"><svg width="12" height="14" viewBox="0 0 12 16"><path fill="#555" d="M6 0a6 6 0 0 0-6 6c0 4.5 6 10 6 10s6-5.5 6-10a6 6 0 0 0-6-6zm0 8.5A2.5 2.5 0 1 1 6 3.5a2.5 2.5 0 0 1 0 5z"/></svg><span>48 Cedar Avenue, Unit 2, Oak Hill, NY 10002</span></div>
        <div class="loc-row"><svg width="12" height="12" viewBox="0 0 24 24"><path fill="#555" d="M6.6 10.8a15 15 0 0 0 6.6 6.6l2.2-2.2c.3-.3.7-.4 1-.2 1.1.4 2.3.6 3.6.6.6 0 1 .4 1 1V20c0 .6-.4 1-1 1A17 17 0 0 1 3 4c0-.6.4-1 1-1h3.5c.6 0 1 .4 1 1 0 1.3.2 2.5.6 3.6.1.3 0 .7-.2 1z"/></svg><span>123-456-784</span></div>
        <span class="map-link">View Map</span></div>
      <div class="location-card"><h3>Location 3</h3>
        <div class="loc-row"><svg width="12" height="14" viewBox="0 0 12 16"><path fill="#555" d="M6 0a6 6 0 0 0-6 6c0 4.5 6 10 6 10s6-5.5 6-10a6 6 0 0 0-6-6zm0 8.5A2.5 2.5 0 1 1 6 3.5a2.5 2.5 0 0 1 0 5z"/></svg><span>305 Maple Road, Floor 1, Westbrook, NY 10003</span></div>
        <div class="loc-row"><svg width="12" height="12" viewBox="0 0 24 24"><path fill="#555" d="M6.6 10.8a15 15 0 0 0 6.6 6.6l2.2-2.2c.3-.3.7-.4 1-.2 1.1.4 2.3.6 3.6.6.6 0 1 .4 1 1V20c0 .6-.4 1-1 1A17 17 0 0 1 3 4c0-.6.4-1 1-1h3.5c.6 0 1 .4 1 1 0 1.3.2 2.5.6 3.6.1.3 0 .7-.2 1z"/></svg><span>123-456-785</span></div>
        <span class="map-link">View Map</span></div>
      <div class="location-card"><h3>Location 4</h3>
        <div class="loc-row"><svg width="12" height="14" viewBox="0 0 12 16"><path fill="#555" d="M6 0a6 6 0 0 0-6 6c0 4.5 6 10 6 10s6-5.5 6-10a6 6 0 0 0-6-6zm0 8.5A2.5 2.5 0 1 1 6 3.5a2.5 2.5 0 0 1 0 5z"/></svg><span>77 Birch Lane, Suite 9, Millbrook, NY 10004</span></div>
        <div class="loc-row"><svg width="12" height="12" viewBox="0 0 24 24"><path fill="#555" d="M6.6 10.8a15 15 0 0 0 6.6 6.6l2.2-2.2c.3-.3.7-.4 1-.2 1.1.4 2.3.6 3.6.6.6 0 1 .4 1 1V20c0 .6-.4 1-1 1A17 17 0 0 1 3 4c0-.6.4-1 1-1h3.5c.6 0 1 .4 1 1 0 1.3.2 2.5.6 3.6.1.3 0 .7-.2 1z"/></svg><span>123-456-786</span></div>
        <span class="map-link">View Map</span></div>
      <div class="location-card"><h3>Location 5</h3>
        <div class="loc-row"><svg width="12" height="14" viewBox="0 0 12 16"><path fill="#555" d="M6 0a6 6 0 0 0-6 6c0 4.5 6 10 6 10s6-5.5 6-10a6 6 0 0 0-6-6zm0 8.5A2.5 2.5 0 1 1 6 3.5a2.5 2.5 0 0 1 0 5z"/></svg><span>210 Elm Street, Unit 6, Stonefield, NY 10005</span></div>
        <div class="loc-row"><svg width="12" height="12" viewBox="0 0 24 24"><path fill="#555" d="M6.6 10.8a15 15 0 0 0 6.6 6.6l2.2-2.2c.3-.3.7-.4 1-.2 1.1.4 2.3.6 3.6.6.6 0 1 .4 1 1V20c0 .6-.4 1-1 1A17 17 0 0 1 3 4c0-.6.4-1 1-1h3.5c.6 0 1 .4 1 1 0 1.3.2 2.5.6 3.6.1.3 0 .7-.2 1z"/></svg><span>123-456-787</span></div>
        <span class="map-link">View Map</span></div>
      <div class="location-card"><h3>Location 6</h3>
        <div class="loc-row"><svg width="12" height="14" viewBox="0 0 12 16"><path fill="#555" d="M6 0a6 6 0 0 0-6 6c0 4.5 6 10 6 10s6-5.5 6-10a6 6 0 0 0-6-6zm0 8.5A2.5 2.5 0 1 1 6 3.5a2.5 2.5 0 0 1 0 5z"/></svg><span>9 Willow Court, Suite 3, Eastgate, NY 10006</span></div>
        <div class="loc-row"><svg width="12" height="12" viewBox="0 0 24 24"><path fill="#555" d="M6.6 10.8a15 15 0 0 0 6.6 6.6l2.2-2.2c.3-.3.7-.4 1-.2 1.1.4 2.3.6 3.6.6.6 0 1 .4 1 1V20c0 .6-.4 1-1 1A17 17 0 0 1 3 4c0-.6.4-1 1-1h3.5c.6 0 1 .4 1 1 0 1.3.2 2.5.6 3.6.1.3 0 .7-.2 1z"/></svg><span>123-456-788</span></div>
        <span class="map-link">View Map</span></div>
      <div class="location-card"><h3>Location 7</h3>
        <div class="loc-row"><svg width="12" height="14" viewBox="0 0 12 16"><path fill="#555" d="M6 0a6 6 0 0 0-6 6c0 4.5 6 10 6 10s6-5.5 6-10a6 6 0 0 0-6-6zm0 8.5A2.5 2.5 0 1 1 6 3.5a2.5 2.5 0 0 1 0 5z"/></svg><span>560 Pine Boulevard, Unit 1, Northvale, NY 10007</span></div>
        <div class="loc-row"><svg width="12" height="12" viewBox="0 0 24 24"><path fill="#555" d="M6.6 10.8a15 15 0 0 0 6.6 6.6l2.2-2.2c.3-.3.7-.4 1-.2 1.1.4 2.3.6 3.6.6.6 0 1 .4 1 1V20c0 .6-.4 1-1 1A17 17 0 0 1 3 4c0-.6.4-1 1-1h3.5c.6 0 1 .4 1 1 0 1.3.2 2.5.6 3.6.1.3 0 .7-.2 1z"/></svg><span>123-456-789</span></div>
        <span class="map-link">View Map</span></div>
      <div class="location-card"><h3>Location 8</h3>
        <div class="loc-row"><svg width="12" height="14" viewBox="0 0 12 16"><path fill="#555" d="M6 0a6 6 0 0 0-6 6c0 4.5 6 10 6 10s6-5.5 6-10a6 6 0 0 0-6-6zm0 8.5A2.5 2.5 0 1 1 6 3.5a2.5 2.5 0 0 1 0 5z"/></svg><span>14 Aspen Way, Suite 8, Southport, NY 10008</span></div>
        <div class="loc-row"><svg width="12" height="12" viewBox="0 0 24 24"><path fill="#555" d="M6.6 10.8a15 15 0 0 0 6.6 6.6l2.2-2.2c.3-.3.7-.4 1-.2 1.1.4 2.3.6 3.6.6.6 0 1 .4 1 1V20c0 .6-.4 1-1 1A17 17 0 0 1 3 4c0-.6.4-1 1-1h3.5c.6 0 1 .4 1 1 0 1.3.2 2.5.6 3.6.1.3 0 .7-.2 1z"/></svg><span>123-456-790</span></div>
        <span class="map-link">View Map</span></div>
    </div>
  </div>
</section>

<section class="categories">
  <div class="container">
    <h2 class="section-title">Our Liquor</h2>
    <p class="section-sub">Lorem ipsum dolor sit amet</p>
    <div class="category-list">
      <div class="category">
        <svg width="110" height="150" viewBox="0 0 110 150"><path fill="#6e6e6e" d="M20 40h10V5h10v35h10v105H20zM66 20h8v40l10 15v70H56V75l10-15z"/></svg>
        Fine Wines</div>
      <div class="category">
        <svg width="140" height="150" viewBox="0 0 140 150"><path fill="#6e6e6e" d="M10 60l14-20V20h12v20l14 20v85H10zM55 30h30v20l10 15v80H45V65l10-15zM100 55h10v25l14 15v50H86V95l14-15z"/></svg>
        Spirits</div>
      <div class="category">
        <svg width="150" height="150" viewBox="0 0 150 150"><path fill="#6e6e6e" d="M10 20h40l-6 50a14 14 0 0 1-10 12v50h12v8H14v-8h12V82a14 14 0 0 1-10-12zM60 40h30v80a15 15 0 0 1-30 0zM100 20h40l-6 50a14 14 0 0 1-10 12v50h12v8h-32v-8h12V82a14 14 0 0 1-10-12z"/></svg>
        Cold Beers</div>
      <div class="category">
        <svg width="110" height="150" viewBox="0 0 110 150"><path fill="#6e6e6e" d="M10 60h90v85H10zM25 10h10v45H25zM45 5h10v50H45zM65 10h10v45H65z"/><path fill="#fff" d="M10 60l90 40v10L10 70z"/></svg>
        Cigars</div>
    </div>
  </div>
</section>

<section class="testimonials">
  <div class="container">
    <div class="quote-badge">“</div>
    <div class="testimonial-list">
      <div class="testimonial">
        <div class="testimonial-head"><div class="avatar" role="img" aria-label="Customer portrait"></div><p>Great selection and friendly staff, always find the bottle I want at a fair price here.</p></div>
        <div class="name">JENNA</div>
      </div>
      <div class="testimonial">
        <div class="testimonial-head"><div class="avatar" role="img" aria-label="Customer portrait"></div><p>The walk in beer cave is amazing and the cigar humidor is kept in perfect condition.</p></div>
        <div class="name">ROWAN</div>
      </div>
      <div class="testimonial">
        <div class="testimonial-head"><div class="avatar" role="img" aria-label="Customer portrait"></div><p>Helpful advice on wine pairings every time, and quick service at all of the locations.</p></div>
        <div class="name">MARA</div>
      </div>
    </div>
    <div class="dots"><span></span><span></span><span></span></div>
  </div>
</section>

<section class="products">
  <div class="container">
    <h2 class="section-title">Our Popular Liquor</h2>
    <p class="section-sub">Lorem ipsum dolor sit amet</p>
    <div class="product-grid">
      <div class="product-card"><div class="product-photo" role="img" aria-label="Three dark wine bottles"></div><p class="product-name">2000 YSJ Reserve Rosa<br>of Syrah</p><p class="price">$70</p></div>
      <div class="product-card"><div class="product-photo" role="img" aria-label="Three dark wine bottles"></div><p class="product-name">2000 YSJ Reserve Rosa<br>of Syrah</p><p class="price">$70</p></div>
      <div class="product-card"><div class="product-photo" role="img" aria-label="Three dark wine bottles"></div><p class="product-name">2000 YSJ Reserve Rosa<br>of Syrah</p><p class="price">$70</p></div>
      <div class="product-card"><div class="product-photo" role="img" aria-label="Three dark wine bottles"></div><p class="product-name">2000 YSJ Reserve Rosa<br>of Syrah</p><p class="price">$70</p></div>
      <div class="product-card"><div class="product-photo" role="img" aria-label="Three dark wine bottles"></div><p class="product-name">2000 YSJ Reserve Rosa<br>of Syrah</p><p class="price">$70</p></div>
      <div class="product-card"><div class="product-photo" role="img" aria-label="Three dark wine bottles"></div><p class="product-name">2000 YSJ Reserve Rosa<br>of Syrah</p><p class="price">$70</p></div>
    </div>
  </div>
</section>

<section class="blog">
  <h2 class="section-title">Our Latest Blog</h2>
  <div class="title-rule"></div>
  <p class="section-sub">Lorem ipsum dolor sit amet, consectetur adipiscing elit, sed do eiusmod tempor incididunt ut labore et dolore magna aliqua. Ut enim ad minim veniam, quis nostrud exercitation ullamco laboris.</p>
  <div class="blog-grid">
    <article class="post">
      <div class="post-photo" role="img" aria-label="Beer glasses and snacks on a bar counter" style="background:linear-gradient(135deg,#5a3a22,#c98a3f 55%,#3a2616)"></div>
      <div class="post-meta">Lorem Ipsum<br><span class="date">January 12, 2019</span></div>
      <p>Lorem ipsum dolor sit amet, consectetur adipiscing elit, sed do eiusmod tempor incididunt ut labore et dolore magna aliqua.</p>
      <span class="read-more">Read more</span>
    </article>
    <article class="post">
      <div class="post-photo" role="img" aria-label="Friends toasting drinks in a bar" style="background:linear-gradient(135deg,#2c1a14,#a0533a 50%,#1e1412)"></div>
      <div class="post-meta">Lorem Ipsum<br><span class="date">January 12, 2019</span></div>
      <p>Lorem ipsum dolor sit amet, consectetur adipiscing elit, sed do eiusmod tempor incididunt ut labore et dolore magna aliqua.</p>
      <span class="read-more">Read more</span>
    </article>
    <article class="post">
      <div class="post-photo" role="img" aria-label="Group celebrating with drinks under warm lights" style="background:linear-gradient(135deg,#3a2a4a,#d4a35a 50%,#241a2e)"></div>
      <div class="post-meta">Lorem Ipsum<br><span class="date">January 12, 2019</span></div>
      <p>Lorem ipsum dolor sit amet, consectetur adipiscing elit, sed do eiusmod tempor incididunt ut labore et dolore magna aliqua.</p>
      <span class="read-more">Read more</span>
    </article>
  </div>
</section>

<footer class="site-footer">
  <div class="container footer-cols">
    <div class="footer-col">
      <h4>COPPERFEN HOLLOW</h4>
      <p>Lorem ipsum dolor sit amet, consectetur adipiscing elit, sed do eiusmod tempor incididunt ut labore et dolore magna aliqua. Ut enim ad minim veniam, quis nostrud exercitation.</p>
    </div>
    <div class="footer-col">
      <h4>RECENT PRODUCTS</h4>
      <ul><li>Product 1</li><li>Product 2</li><li>Product 3</li><li>Product 4</li><li>Product 5</li><li>Product 6</li><li>Product 7</li></ul>
    </div>
    <div class="footer-col">
      <h4>USEFUL LINKS</h4>
      <ul><li>Home</li><li>Fine Wines</li><li>Spirits</li><li>Cold Beers</li><li>Cigars</li><li>About Us</li><li>Contact Us</li></ul>
    </div>
    <div class="footer-col">
      <h4>CONTACT WITH US</h4>
      <div class="contact-line"><svg width="14" height="14" viewBox="0 0 24 24"><path fill="#fff" d="M6.6 10.8a15 15 0 0 0 6.6 6.6l2.2-2.2c.3-.3.7-.4 1-.2 1.1.4 2.3.6 3.6.6.6 0 1 .4 1 1V20c0 .6-.4 1-1 1A17 17 0 0 1 3 4c0-.6.4-1 1-1h3.5c.6 0 1 .4 1 1 0 1.3.2 2.5.6 3.6.1.3 0 .7-.2 1z"/></svg>123-456-783</div>
      <div class="contact-line"><svg width="14" height="12" viewBox="0 0 24 18"><path fill="#fff" d="M0 0h24v18H0zm2 2v1l10 7 10-7V2z"/></svg>info@copperfenhollow.com</div>
      <div class="contact-line"><svg width="12" height="14" viewBox="0 0 12 16"><path fill="#fff" d="M6 0a6 6 0 0 0-6 6c0 4.5 6 10 6 10s6-5.5 6-10a6 6 0 0 0-6-6zm0 8.5A2.5 2.5 0 1 1 6 3.5a2.5 2.5 0 0 1 0 5z"/></svg><span>PO Box 2047, Hollow Road<br>Riverside Park, NY 10001</span></div>
    </div>
  </div>
</footer>

<div class="bottom-bar">
  <div class="container">
    <span>Copyright © 2019 All rights reserved</span>
    <div class="socials"><span></span><span></span><span></span></div>
  </div>
</div>

</body>
</html>
```